family chiropractic health care team needs a modern business card design

Healthcare office with Chiropractors, Physiotherapists, Massage therapists and possibly other practitioners in the future. This is a friendly family office with patients of all ages (and lots of kids) that just moved into a new larger modern office.
Look at the website for photos of the office.
Design for the front and back of a business card required.
Text for the front:
Office logo and name of the office:
Bright Path Wellness Centre
Name of current Practitioner:
Dr. Marten Quogue B.Sc., D.C. Chiropractor
(But please include options to swap out name and title for other practitioners )

address:
217 Tamsey Road
Etobicoke ON.
K2R 6P4
Phone: 416-870-2961 (MOVE)
Web site and email:
www.brightpathwellcentre.example
brightpathchiro@mailnest.example

2 versions of the back of the card:
1. text below
2. appointment schedule card

Text on back of card:
Chiropractic Card text on back of the card:
There is more to chiropractic than the relief of headaches and back pain! Our primary focus is the integrity of your nerve system, which controls and regulates every cell and tissue of your body. The moving bones of the spinal column can impair this vital communication link between your brain and body. We help improve the function and structure of your spine, reducing nerve system compromise. The result?
Even non-spinal related health problems can show improvement
without drugs
without surgery
regardless of age
for over a century
naturally

Appointment Card info For Back:
Please integrate design elements from the front of the card into an appointment card format.
M Tu W Th F Sat (and a line for writing on beside each one)

```html
<!DOCTYPE html>
<html lang="en">
<head>
<meta charset="utf-8">
<title>Bright Path Wellness Centre – Business Card</title>
<link href="https://fonts.googleapis.com/css2?family=Libre+Baskerville:wght@400;700&family=Open+Sans:wght@400;600&display=swap" rel="stylesheet">
<style>
  :root {
    --leaf-green: #7ab648;
    --ink-grey: #8a8b8d;
    --ink-dark: #1e1e1e;
    --card-white: #ffffff;
    --backdrop: #e9e6e0;
    --rule-grey: #3a3a3a;
  }
  * { box-sizing: border-box; margin: 0; padding: 0; }
  html, body { width: 1200px; height: 900px; overflow: hidden; }
  body {
    background: var(--backdrop);
    position: relative;
    font-family: "Open Sans", Arial, sans-serif;
    color: var(--ink-dark);
  }
  .card {
    position: absolute;
    left: 280px;
    width: 640px;
    height: 366px;
    background: var(--card-white);
    box-shadow: 0 6px 18px rgba(0,0,0,0.12);
    overflow: hidden;
  }
  .card--back { top: 60px; }
  .card--front { top: 474px; }

  /* Appointment side */
  .appointment-title {
    position: absolute; top: 34px; left: 0; right: 0;
    text-align: center;
    font-family: "Libre Baskerville", Georgia, serif;
    font-weight: 700; font-size: 19px;
    color: var(--leaf-green);
  }
  .write-line {
    position: absolute; left: 48px; right: 48px;
    border-bottom: 1px solid var(--rule-grey);
    font-family: "Libre Baskerville", Georgia, serif;
    font-size: 13px; color: var(--ink-dark);
    height: 22px;
  }
  .write-line__label { position: absolute; bottom: 3px; background: var(--card-white); padding-right: 6px; }
  .write-line__label--date { left: 0; }
  .write-line__label--time { left: 290px; padding-left: 6px; }
  .write-line--date { top: 72px; }
  .write-line--two { top: 112px; }
  .write-line--three { top: 148px; }
  .write-line--four { top: 184px; }
  .day-row {
    position: absolute; top: 224px; left: 70px; right: 70px;
    display: flex; justify-content: space-between;
    font-family: "Libre Baskerville", Georgia, serif; font-size: 13px;
  }
  .day { display: flex; align-items: center; gap: 8px; }
  .day__box { width: 11px; height: 11px; border: 1px solid var(--ink-dark); }
  .back-note {
    position: absolute; top: 276px; left: 90px; right: 90px;
    text-align: center; font-size: 12.5px; line-height: 1.45;
    color: var(--ink-dark);
  }

  /* Front side */
  .brand {
    position: absolute; top: 92px; left: 56px;
    display: flex; align-items: center; gap: 10px;
  }
  .brand__mark { width: 20px; height: 20px; border-radius: 50%; background: var(--leaf-green); flex: none; }
  .brand__name {
    font-family: "Libre Baskerville", Georgia, serif;
    font-weight: 700; font-size: 20px; color: var(--leaf-green);
    white-space: nowrap;
  }
  .brand-rule {
    position: absolute; top: 132px; left: 56px; width: 300px;
    height: 1px; background: var(--ink-grey);
  }
  .practitioner {
    position: absolute; top: 146px; right: 36px; text-align: right;
    white-space: nowrap;
  }
  .practitioner__name {
    font-family: "Libre Baskerville", Georgia, serif;
    font-weight: 700; font-size: 18px; color: var(--leaf-green);
  }
  .practitioner__title {
    font-family: "Libre Baskerville", Georgia, serif;
    font-size: 12px; color: var(--ink-dark); margin-top: 4px;
  }
  .accent-rule {
    position: absolute; top: 186px; left: 56px; width: 320px;
    height: 2px; background: var(--leaf-green);
  }
  .contact-list {
    position: absolute; top: 210px; left: 56px;
    list-style: none;
  }
  .contact-list__item {
    display: flex; align-items: center; gap: 14px;
    font-size: 15px; line-height: 1; height: 28px;
    white-space: nowrap;
  }
  .contact-list__icon {
    width: 16px; height: 16px; background: var(--leaf-green);
    display: flex; align-items: center; justify-content: center;
    flex: none;
  }
  .contact-list__icon svg { width: 11px; height: 11px; }
</style>
</head>
<body>

<section class="card card--back" aria-label="Appointment card, back side">
  <h2 class="appointment-title">Appointment</h2>
  <div class="write-line write-line--date">
    <span class="write-line__label write-line__label--date">Date</span>
    <span class="write-line__label write-line__label--time">Time</span>
  </div>
  <div class="write-line write-line--two"></div>
  <div class="write-line write-line--three"></div>
  <div class="write-line write-line--four"></div>
  <div class="day-row">
    <span class="day"><span class="day__box"></span>Mon</span>
    <span class="day"><span class="day__box"></span>Tues</span>
    <span class="day"><span class="day__box"></span>Wed</span>
    <span class="day"><span class="day__box"></span>Thu</span>
    <span class="day"><span class="day__box"></span>Sat</span>
  </div>
  <p class="back-note">Even non-spinal related health problems can show improvement without drugs, without surgery, regardless of age for over a century naturally.</p>
</section>

<section class="card card--front" aria-label="Business card, front side">
  <div class="brand">
    <span class="brand__mark"></span>
    <span class="brand__name">Bright Path Wellness Centre</span>
  </div>
  <div class="brand-rule"></div>
  <div class="practitioner">
    <div class="practitioner__name">Dr. Marten Quogue</div>
    <div class="practitioner__title">B.Sc., D.C. Chiropractor</div>
  </div>
  <div class="accent-rule"></div>
  <ul class="contact-list">
    <li class="contact-list__item">
      <span class="contact-list__icon"><svg viewBox="0 0 12 12"><path d="M2.5 1h2l1 2.5-1.2 1a6 6 0 0 0 3.2 3.2l1-1.2 2.5 1v2c0 .6-.4 1-1 1A9 9 0 0 1 1.5 2c0-.6.4-1 1-1z" fill="#fff"/></svg></span>
      416-870-2961
    </li>
    <li class="contact-list__item">
      <span class="contact-list__icon"><svg viewBox="0 0 12 12"><circle cx="6" cy="6" r="4.6" fill="none" stroke="#fff" stroke-width="1.1"/><ellipse cx="6" cy="6" rx="2" ry="4.6" fill="none" stroke="#fff" stroke-width="1"/><line x1="1.4" y1="6" x2="10.6" y2="6" stroke="#fff" stroke-width="1"/></svg></span>
      www.brightpathwellcentre.example
    </li>
    <li class="contact-list__item">
      <span class="contact-list__icon"><svg viewBox="0 0 12 12"><rect x="1" y="2.5" width="10" height="7" fill="none" stroke="#fff" stroke-width="1.1"/><path d="M1 2.8 6 6.6 11 2.8" fill="none" stroke="#fff" stroke-width="1.1"/></svg></span>
      brightpathchiro@mailnest.example
    </li>
    <li class="contact-list__item">
      <span class="contact-list__icon"><svg viewBox="0 0 12 12"><path d="M6 11S2.3 7 2.3 4.6a3.7 3.7 0 0 1 7.4 0C9.7 7 6 11 6 11z" fill="#fff"/><circle cx="6" cy="4.6" r="1.3" fill="#7ab648"/></svg></span>
      217 Tamsey Road Etobicoke ON. K2R 6P4
    </li>
  </ul>
</section>

</body>
</html>
```